Design "RIDGEMANTIS" Shopify online store for hunting, outdoor and tactical accessories, appare

Design and setup Shopify platform online store for hunting, outdoor and tactical accessories, apparel.

Logo has been uploaded. Social, Facebook and domain all setuop

A really modern easy to navigate online store that I can add and remove categories, add and remove products, update images, slider images, must have a AUD, USD, EUR, NZD and GBP currency converter drop down. RRPs will start in AUD. domain name is already registered and logo is done. Products are being photographed in readiness for you to set up the site. Fast shopping cart as guest with just name and address vs joining and collecting info for newsletters. Ability to send out newsletters. Home page that showcases 4-6 key categories of the site with hero images that can be updated by me. A clear navigation pane across the top. In the shopping part a clear categories navigation that can be updated as required. Free postage Australia and NZ, international shipment extra. Ultimately I need a great design as we have great products appealing to hunters, people who love the outdoors from camping to hiking, to tactical supplies. It's important to be strong website that shows quality and is easy to get arouund. Most of all it is brand new so whatever you can do to help drive traffic to it please do so. I will be managing it when ready with view to hiring a social media/web analyst to support me in a month.

Target Market(s)

Australian hunters and outdoor lovers - camping, hiking, motorbikes (dirt bikes / MX), and tactical professionals

Industry/Entity Type

Online Shopping

Coding

Coded - Design and coding required

Number of Pages Required

5+ page

Requirements
Must have
• As per my description plus up to the designers. You are the experts. I want it to look great but ultimately it has to get traffic and SELL PRODUCT
• Would like option for people to review products, eg leave 1-5 stars.
• After pay and Paypal for payment is my suggestion but I'm not the expert
• Work on computers, tablets and smartphones - compatible for all devices
Nice to have
• Product thumbnails, rankings. Can click on product to see more pictures, video and details. Size charts for apparel.
• Products will be things such as bags, equipment, accessories, clothing - all designed for outdoor activities predominantly hunting, camping, MX dirt bike riding, fishing, etc

```html
<!DOCTYPE html>
<html lang="en">
<head>
<meta charset="utf-8">
<title>Ridgemantis – Live for the Hunt</title>
<link href="https://fonts.googleapis.com/css2?family=Poppins:wght@400;500;600;700&family=Lora:ital,wght@0,400;0,500;1,400&display=swap" rel="stylesheet">
<style>
:root{
  --orange:#f26a10;
  --black:#0b0b0b;
  --ink:#1c1c1c;
  --grey:#6b6b6b;
  --light:#f1f1f1;
  --line:#d9d9d9;
  --white:#ffffff;
}
*{box-sizing:border-box;margin:0;padding:0}
html,body{width:1200px;height:4079px;overflow:hidden}
body{font-family:"Poppins",sans-serif;color:var(--ink);background:var(--white);position:relative}

/* top bar */
.topbar{position:absolute;top:0;left:0;width:1200px;height:33px;background:var(--orange);color:var(--white);font-size:11px;font-weight:500;display:flex;align-items:center;justify-content:space-between;padding:0 118px}
.topbar .links{display:flex;gap:18px;text-transform:uppercase}

/* header */
.header{position:absolute;top:33px;left:0;width:1200px;height:125px;background:var(--black)}
.brand{position:absolute;left:118px;top:38px;display:flex;align-items:center;gap:12px;color:var(--white);font-weight:700;font-size:34px;letter-spacing:1px}
.brand .mark{width:26px;height:26px;background:var(--orange)}
.header-tools{position:absolute;right:118px;top:48px;display:flex;align-items:center;gap:18px;color:var(--white);font-size:13px}
.header-tools svg{display:block}

/* nav */
.nav{position:absolute;top:158px;left:0;width:1200px;height:52px;background:var(--white);border-bottom:1px solid var(--line);display:flex;justify-content:center;align-items:center;font-size:13px;font-weight:500;text-transform:uppercase}
.nav a{padding:0 20px;color:var(--ink);text-decoration:none;border-right:1px solid #bbb;line-height:16px}
.nav a:last-child{border-right:none}
.nav a.active{color:var(--orange)}
.nav .caret{font-size:9px;margin-left:4px}

/* hero */
.hero{position:absolute;top:210px;left:0;width:1200px;height:536px;background:radial-gradient(ellipse at 50% 40%,#6a6a62 0%,#55534a 45%,#4a4536 100%)}
.hero-title{position:absolute;top:440px;width:1200px;text-align:center;color:var(--white);font-weight:600;font-size:68px;letter-spacing:2px}
.hero-sub{position:absolute;top:528px;width:1200px;text-align:center;color:var(--white);font-size:22px;letter-spacing:.5px}
.btn-ghost{position:absolute;left:454px;top:598px;width:289px;height:44px;background:#111;border:1px solid #888;color:var(--white);font-size:14px;font-weight:500;display:flex;align-items:center;justify-content:center;letter-spacing:.5px}

/* section headings */
.sec-title{position:absolute;width:1200px;text-align:center;font-weight:700;font-size:27px;letter-spacing:.5px;text-transform:uppercase}
.rule{position:absolute;left:480px;width:240px;height:12px}
.rule::before,.rule::after{content:"";position:absolute;top:6px;width:100px;height:1px;background:#777}
.rule::before{left:0}.rule::after{right:0}
.rule span{position:absolute;left:112px;top:0;width:16px;height:12px;border-bottom:2px solid #444;border-left:2px solid transparent;border-right:2px solid transparent}

.intro{position:absolute;top:878px;left:300px;width:600px;text-align:center;font-family:"Lora",serif;font-style:italic;font-size:12.5px;line-height:19px;color:#333}

/* categories */
.tile{position:absolute}
.tile-label{position:absolute;background:var(--orange);color:var(--white);font-weight:500;font-size:14px;letter-spacing:1px;display:flex;align-items:center;justify-content:center;text-transform:uppercase}
.promo{position:absolute;top:1467px;left:122px;width:950px;height:38px;background:var(--black);color:var(--white);font-size:12px;font-weight:500;display:flex;align-items:center;justify-content:center;letter-spacing:.5px}
.promo b{color:var(--orange);font-weight:600;margin-left:4px}

/* products */
.product{position:absolute;top:1671px;width:217px}
.product .photo{width:217px;height:275px;background:linear-gradient(180deg,#4c5a3e 0%,#2c2c2a 55%,#b9a36a 80%,#2a2a2a 100%);position:relative}
.product .tools{position:absolute;right:10px;top:12px;display:flex;flex-direction:column;gap:8px}
.product .name{margin-top:18px;font-family:"Lora",serif;font-style:italic;font-size:14px;padding-bottom:8px;border-bottom:1px solid var(--line);width:150px}
.product .meta{margin-top:8px;display:flex;justify-content:space-between;align-items:center;font-size:11px;color:var(--grey)}
.dots{display:flex;gap:4px}
.dots i{width:11px;height:11px;border-radius:50%;display:block}
.arrow{position:absolute;top:1779px;width:52px;height:52px;border:1px solid #999;border-radius:50%;display:flex;align-items:center;justify-content:center;background:var(--white)}

/* newsletter */
.newsletter{position:absolute;top:2079px;left:0;width:1200px;height:411px;background:radial-gradient(ellipse at 50% 50%,#3a3834 0%,#22211f 60%,#151514 100%)}
.nl-kicker{position:absolute;top:2135px;width:1200px;text-align:center;color:var(--white);font-size:21px}
.nl-title{position:absolute;top:2170px;width:1200px;text-align:center;color:var(--white);font-family:"Lora",serif;font-size:40px}
.nl-text{position:absolute;top:2240px;left:380px;width:440px;text-align:center;color:var(--white);font-size:13px;line-height:20px}
.nl-input{position:absolute;top:2340px;left:264px;width:503px;height:41px;border-bottom:2px solid var(--orange);display:flex;align-items:center;gap:12px;color:#aaa;font-size:13px;padding-left:4px}
.nl-btn{position:absolute;top:2340px;left:770px;width:163px;height:41px;background:var(--orange);color:var(--white);font-weight:500;font-size:14px;display:flex;align-items:center;justify-content:center;letter-spacing:1px}

/* news */
.post{position:absolute;top:2639px;width:300px;text-align:center}
.post .photo{height:218px;background:linear-gradient(180deg,#b7c5cf 0%,#c9c0a4 50%,#9c8c62 100%)}
.post h3{margin-top:34px;font-family:"Lora",serif;font-weight:400;font-size:20px}
.post .by{margin-top:6px;font-size:12px;color:#444}
.post .by b{color:var(--orange);font-weight:400}
.post p{margin-top:12px;font-size:12px;line-height:17px;color:#444;padding:0 4px}
.btn-more{position:absolute;top:3072px;left:498px;width:201px;height:41px;background:var(--orange);color:var(--white);font-size:13px;font-weight:500;display:flex;align-items:center;justify-content:center;letter-spacing:.5px}

/* testimonial */
.t-title{position:absolute;top:3196px;left:120px;width:446px;text-align:center;font-size:25px;font-weight:500;text-transform:uppercase}
.avatar{position:absolute;top:3268px;left:303px;width:80px;height:80px;border-radius:50%;background:radial-gradient(circle at 50% 40%,#c89a7c 0%,#5a3a2a 100%)}
.t-quote{position:absolute;top:3370px;left:135px;width:416px;text-align:center;font-size:12px;line-height:17px;color:#444}
.t-name{position:absolute;top:3437px;left:120px;width:446px;text-align:center;font-size:12px;color:#444}
.t-dots{position:absolute;top:3476px;left:330px;display:flex;gap:8px}
.t-dots i{width:8px;height:8px;border-radius:50%;background:#bbb;display:block}
.t-dots i:first-child{background:#333}
.feed{position:absolute;top:3181px;left:601px;width:460px;height:310px;display:grid;grid-template-columns:repeat(3,1fr);grid-template-rows:repeat(2,1fr);gap:8px}
.feed div{background:linear-gradient(135deg,#d9d0c6,#a99886)}

/* partners */
.partners{position:absolute;top:3537px;left:0;width:1200px;height:96px;background:var(--light);display:flex;align-items:center;padding-left:150px;font-size:17px}
.partners .lead{width:180px;letter-spacing:1.5px;border-right:1px solid #999;line-height:30px;margin-right:40px;font-size:16px}
.partners .names{display:flex;gap:62px;font-weight:500;letter-spacing:1px}

/* footer */
.footer{position:absolute;top:3633px;left:0;width:1200px;height:446px;background:var(--black);color:var(--white)}
.f-brand{position:absolute;top:70px;width:1200px;display:flex;justify-content:center;align-items:center;gap:12px;font-weight:700;font-size:34px;letter-spacing:1px}
.f-brand .mark{width:26px;height:26px;background:var(--orange)}
.f-col{position:absolute;top:160px;font-size:11px}
.f-col h4{font-size:12px;font-weight:600;letter-spacing:1px;margin-bottom:10px;text-transform:uppercase}
.f-col h4::after{content:"";display:block;width:22px;height:2px;background:var(--orange);margin-top:6px}
.f-col li{list-style:none;line-height:26px;color:#ccc}
.f-col p{color:#ccc;line-height:17px;width:290px;margin-bottom:10px}
.cards{display:flex;gap:6px;margin-top:10px}
.cards span{width:38px;height:24px;border-radius:3px;background:#e6e6e6;display:block}
.copy{position:absolute;top:410px;width:1200px;text-align:center;font-size:11px;color:#bbb}
</style>
</head>
<body>

<div class="topbar">
  <div>OUR PHONE NUMBERS &nbsp; +61 (02) 5550 0148</div>
  <div class="links"><span>My Account</span><span>Cart</span><span>Our Location</span><span>Contact Us</span><span>AUD ▾</span></div>
</div>

<header class="header">
  <div class="brand"><span class="mark"></span>RIDGEMANTIS</div>
  <div class="header-tools">
    <svg width="18" height="18" viewBox="0 0 18 18" fill="none" stroke="#fff" stroke-width="2"><circle cx="7.5" cy="7.5" r="5.5"/><path d="M12 12l5 5"/></svg>
    <svg width="18" height="16" viewBox="0 0 18 16"><path d="M9 15S1 10 1 5a4 4 0 0 1 8-1 4 4 0 0 1 8 1c0 5-8 10-8 10z" fill="#fff"/></svg>
    <svg width="20" height="18" viewBox="0 0 20 18" fill="#fff"><path d="M0 1h4l3 10h10l2-7H6" stroke="#fff" stroke-width="2" fill="none"/><circle cx="8" cy="15" r="2"/><circle cx="16" cy="15" r="2"/></svg>
    <span>0/0.00 AUD</span>
  </div>
</header>

<nav class="nav">
  <a class="active">Home</a>
  <a>Apparel<span class="caret">▾</span></a>
  <a>Accessories<span class="caret">▾</span></a>
  <a>Equipment<span class="caret">▾</span></a>
  <a>Tactical Gears<span class="caret">▾</span></a>
  <a>Contact</a>
</nav>

<section class="hero" role="img" aria-label="Hunter's rifle resting beside a large game animal on dry ground"></section>
<h1 class="hero-title">LIVE FOR THE HUNT</h1>
<div class="hero-sub">APPAREL, ACCESORIES, EQUIPMENT AND TACTICAL GEAR</div>
<div class="btn-ghost">SEE COLLECTION</div>

<h2 class="sec-title" style="top:786px">Featured Categories</h2>
<div class="rule" style="top:836px"><span></span></div>
<p class="intro">Lorem ipsum dolor sit amet esta ada m aria. We provide all kind of Hunting Apparels, Accessories, equipments and tactical gears. Please visit our shop page to see our whole collection</p>

<div class="tile" style="left:122px;top:966px;width:463px;height:468px;background:linear-gradient(160deg,#8fb0d6 0%,#6d8a4d 55%,#3b4a2a 100%)" role="img" aria-label="Hunter in the woods looking through binoculars"></div>
<div class="tile-label" style="left:272px;top:1358px;width:169px;height:35px">Apparels</div>
<div class="tile" style="left:604px;top:966px;width:226px;height:226px;background:linear-gradient(160deg,#4c7a3a,#1f3318)" role="img" aria-label="Hunting knife among green foliage"></div>
<div class="tile-label" style="left:634px;top:1116px;width:166px;height:32px">Accessories</div>
<div class="tile" style="left:604px;top:1208px;width:226px;height:226px;background:linear-gradient(160deg,#4a4a44,#1c1c1a)" role="img" aria-label="Close view of a rifle scope and gear"></div>
<div class="tile-label" style="left:634px;top:1358px;width:166px;height:32px">Equipments</div>
<div class="tile" style="left:849px;top:966px;width:223px;height:468px;background:linear-gradient(180deg,#1e2a4a 0%,#6a4a5a 45%,#e0782a 75%,#2a2620 100%)" role="img" aria-label="Camouflaged hunter with binoculars at sunset"></div>
<div class="tile-label" style="left:878px;top:1358px;width:165px;height:32px">Tactical Gears</div>

<div class="promo">UP TO 70% OFF THE ENTIRE STORE! · MADE WITH LOVE · <b>RIDGEMANTIS</b></div>

<h2 class="sec-title" style="top:1555px">Featured Products</h2>
<div class="rule" style="top:1603px"><span></span></div>

<div class="arrow" style="left:28px"><svg width="14" height="20" viewBox="0 0 14 20" fill="none" stroke="#777" stroke-width="2"><path d="M11 2L3 10l8 8"/></svg></div>
<div class="arrow" style="left:1118px"><svg width="14" height="20" viewBox="0 0 14 20" fill="none" stroke="#777" stroke-width="2"><path d="M3 2l8 8-8 8"/></svg></div>

<div class="product" style="left:125px">
  <div class="photo" role="img" aria-label="Canvas double strap backpack worn by a hunter"></div>
  <div class="name">Backpack Double Strap</div>
  <div class="meta"><span>25$ – 37$ AUD</span><span class="dots"><i style="background:#d32020"></i><i style="background:#1e8a2e"></i></span></div>
</div>
<div class="product" style="left:370px">
  <div class="photo" role="img" aria-label="Canvas double strap backpack worn by a hunter"><div class="tools">
    <svg width="14" height="13" viewBox="0 0 18 16"><path d="M9 15S1 10 1 5a4 4 0 0 1 8-1 4 4 0 0 1 8 1c0 5-8 10-8 10z" fill="none" stroke="#fff" stroke-width="2"/></svg>
    <svg width="14" height="14" viewBox="0 0 18 18" fill="none" stroke="#fff" stroke-width="2"><circle cx="7.5" cy="7.5" r="5.5"/><path d="M12 12l5 5"/></svg></div></div>
  <div class="name">Backpack Double Strap</div>
  <div class="meta"><span>🛒&nbsp; Select Options</span><span class="dots"><i style="background:#d32020"></i><i style="background:#1e8a2e"></i></span></div>
</div>
<div class="product" style="left:615px">
  <div class="photo" role="img" aria-label="Canvas double strap backpack worn by a hunter"><div class="tools">
    <svg width="14" height="13" viewBox="0 0 18 16"><path d="M9 15S1 10 1 5a4 4 0 0 1 8-1 4 4 0 0 1 8 1c0 5-8 10-8 10z" fill="none" stroke="#fff" stroke-width="2"/></svg>
    <svg width="14" height="14" viewBox="0 0 18 18" fill="none" stroke="#fff" stroke-width="2"><circle cx="7.5" cy="7.5" r="5.5"/><path d="M12 12l5 5"/></svg></div></div>
  <div class="name">Backpack Double Strap</div>
  <div class="meta"><span>25$ – 37$ AUD</span><span class="dots"><i style="background:#d32020"></i><i style="background:#1e8a2e"></i></span></div>
</div>
<div class="product" style="left:857px">
  <div class="photo" role="img" aria-label="Canvas double strap backpack worn by a hunter"></div>
  <div class="name">Backpack Double Strap</div>
  <div class="meta"><span>25$ – 37$ AUD</span><span class="dots"><i style="background:#d32020"></i><i style="background:#1e8a2e"></i></span></div>
</div>

<section class="newsletter" role="img" aria-label="Dim forest clearing backdrop"></section>
<div class="nl-kicker">Connect to Ridgemantis</div>
<div class="nl-title">Join Our Newsletter</div>
<p class="nl-text">Hey you, sign up it only takes a second to be the first to find out about our latest news and promotions...</p>
<div class="nl-input"><svg width="14" height="10" viewBox="0 0 14 10" fill="none" stroke="#aaa" stroke-width="1.2"><rect x="0.6" y="0.6" width="12.8" height="8.8"/><path d="M1 1l6 5 6-5"/></svg>Your email id</div>
<div class="nl-btn">SIGN UP</div>

<h2 class="sec-title" style="top:2531px">Latest News</h2>
<div class="rule" style="top:2579px"><span></span></div>

<article class="post" style="left:117px">
  <div class="photo" role="img" aria-label="Dirt bike parked on an open plain"></div>
  <h3>Venenatis veulum peus</h3>
  <div class="by">By <b>Mara Ellison</b> | 2 comments</div>
  <p>Sociosqu scele risque aliquet penatibus pretium vestib bulum imperdiet ad metus a tempus congue a venenatis condi mentum arturient dis</p>
</article>
<article class="post" style="left:447px">
  <div class="photo" role="img" aria-label="Dirt bike parked on an open plain"></div>
  <h3>Venenatis veulum peus</h3>
  <div class="by">By <b>Mara Ellison</b> | 2 comments</div>
  <p>Sociosqu scele risque aliquet penatibus pretium vestib bulum imperdiet ad metus a tempus congue a venenatis condi mentum arturient dis</p>
</article>
<article class="post" style="left:776px">
  <div class="photo" role="img" aria-label="Dirt bike parked on an open plain"></div>
  <h3>Venenatis veulum peus</h3>
  <div class="by">By <b>Mara Ellison</b> | 2 comments</div>
  <p>Sociosqu scele risque aliquet penatibus pretium vestib bulum imperdiet ad metus a tempus congue a venenatis condi mentum arturient dis</p>
</article>
<div class="btn-more">LOAD MORE NEWS</div>

<h2 class="t-title">What they say about us?</h2>
<div class="avatar" role="img" aria-label="Customer portrait"></div>
<p class="t-quote">Fringilla iaculis ante torquent a diam a vestibulum diam nisi augue dictumst parturient a vestibulum tortor viverra inceptos adipiscing nec a ullamcorper ullamcorper aliquam rutrum.</p>
<div class="t-name">John Doe - Happy Customer</div>
<div class="t-dots"><i></i><i></i></div>
<div class="feed" role="img" aria-label="Grid of six lifestyle photos from the store's social feed">
  <div></div><div></div><div></div><div></div><div></div><div></div>
</div>

<div class="partners">
  <div class="lead">OUR PARTNERS</div>
  <div class="names"><span>LARKFIELD</span><span>Wovenly</span><span>CRAG &amp; FERN</span><span>OSTRA</span><span>MARONI</span></div>
</div>

<footer class="footer">
  <div class="f-brand"><span class="mark"></span>RIDGEMANTIS</div>
  <div class="f-col" style="left:122px"><h4>Our Stores</h4><ul><li>New York</li><li>London SF</li><li>Cockfosters BP</li><li>Los Angeles</li><li>Chicago</li><li>Las Vegas</li></ul></div>
  <div class="f-col" style="left:286px"><h4>Information</h4><ul><li>About Store</li><li>Apparels</li><li>Equipments</li><li>Accessories</li><li>Tactical Gears</li><li>Contact Us</li></ul></div>
  <div class="f-col" style="left:449px"><h4>Useful Links</h4><ul><li>Privacy Policy</li><li>Returns</li><li>Terms &amp; Conditions</li><li>Contact Us</li><li>Latest News</li><li>Our Sitemap</li></ul></div>
  <div class="f-col" style="left:610px"><h4>Footer Menu</h4><ul><li>Social profile</li><li>New Collection</li><li>Woman Dress</li><li>Contact Us</li><li>Latest News</li></ul></div>
  <div class="f-col" style="left:773px"><h4>About The Store</h4>
    <p>STORE - worldwide fashion store since 1978. We sell over 1000+ branded products on our website.</p>
    <p>⌖ &nbsp;12 Ironbark Lane, Ballarat VIC<br>✆ &nbsp;Phone: (03) 5550 2217</p>
    <div class="cards"><span></span><span></span><span></span><span></span><span></span><span></span></div>
  </div>
  <div class="copy">© 2017 All rights Reserved | Ridgemantis</div>
</footer>

</body>
</html>
```